依頼詳細
<デザインイメージ>
・ラグジュアリー/高級なイメージ
・VIPのように扱われている
・希少な会に招待されている
記載項目
最低限記載項目:キャッチコピーや見出し/講演タイトル/日時/場所
※講演タイトル/日時/場所については、添付ファイルに記載しています。
※これを使って下さいという素材は特に決まっていません。
サイズ
A4
ページ数
片面
希望イメージ
• +5 0 +5
• シンプル
複雑
• 単色
カラフル
• 暗い
明るい
• 日常
高級
• 遊び心
厳粛
• 未来的
伝統的
• 女性的
男性的
希望する色
黄・オレンジ系、グレー系
納品ファイル
• 高解像度JPG (.jpg)
• イラストレーター形式 (.ai)
• フォトショップ形式 (.psd)
• PNG形式 (.png)
補足説明
依頼公開後の追記内容
<追記>

・講演の内容/テーマ
・講演のスケジュール
・会場について
・チケットの料金
・お申し込み方法
・お問い合わせ先

こちらについては
裏面に記載しております。

チラシ作品として非常に完成度が高かった事に加えて、内容も洗練されていたことが決め手となりました。

この度は、誠に多くのミルダー様にご提案をいただきましたことを、心から感謝いたします。皆様のご提案のクオリティがどれも高く選定にとても悩みました。

この度選定できなかったミルダー様にも、ご縁次第で、また直接ご依頼をさせていただきたいと思っておりますので、今後ともどうぞよろしくお願いいたします。

```html
<!DOCTYPE html>
<html lang="ja">
<head>
<meta charset="utf-8">
<title>BILLIONAIRE LESSON 2018</title>
<link rel="stylesheet" href="https://fonts.googleapis.com/css2?family=Cinzel:wght@400;500&family=Cormorant+Garamond:wght@500;600&family=Noto+Serif+JP:wght@400;500;600&display=swap">
<style>
  :root {
    --ink: #000000;
    --gold: #d8b25c;
    --visual-light: #dfe8f6;
    --visual-mid: #2c4f8c;
    --visual-deep: #081630;
  }
  * { margin: 0; padding: 0; box-sizing: border-box; }
  html, body { width: 851px; height: 1200px; overflow: hidden; background: var(--ink); }
  .poster {
    position: relative; width: 851px; height: 1200px; overflow: hidden;
    background: var(--ink); color: var(--gold);
    font-family: "Noto Serif JP", serif;
  }
  .hero-visual {
    position: absolute; left: 60px; top: 330px; width: 731px; height: 560px;
    background: radial-gradient(ellipse 50% 50% at 50% 45%, var(--visual-light) 0%, var(--visual-mid) 35%, var(--visual-deep) 65%, rgba(0,0,0,0) 100%);
  }
  .title-en {
    position: absolute; left: 22px; font-family: "Cinzel", serif; font-weight: 400;
    font-size: 74px; line-height: 1; letter-spacing: 20px; color: var(--gold);
  }
  .title-en--first { top: 22px; }
  .title-en--second { top: 112px; }
  .divider-slash { position: absolute; left: 0; top: 0; }
  .title-ja {
    position: absolute; left: 26px; top: 208px; font-size: 27px; font-weight: 500;
    letter-spacing: 4px; color: var(--gold);
  }
  .catch {
    position: absolute; top: 150px; writing-mode: vertical-rl;
    font-size: 70px; font-weight: 600; line-height: 1; letter-spacing: 8px;
    color: var(--gold);
  }
  .catch--first { left: 732px; }
  .catch--second { left: 650px; }
  .date {
    position: absolute; left: 22px; top: 860px; display: flex; align-items: baseline;
    font-family: "Cormorant Garamond", serif; font-weight: 600; color: var(--gold);
    font-variant-numeric: lining-nums;
  }
  .date-year { font-size: 64px; letter-spacing: 1px; }
  .date-day { font-size: 120px; line-height: 1; margin-left: 8px; letter-spacing: -1px; }
  .date-week { display: flex; gap: 8px; margin-left: 10px; font-family: "Noto Serif JP", serif; font-size: 34px; font-weight: 600; }
  .date-week .holiday {
    display: inline-flex; width: 42px; height: 42px; border: 2px solid var(--gold);
    border-radius: 50%; align-items: center; justify-content: center; font-size: 27px;
  }
  .tour-label {
    position: absolute; left: 568px; top: 880px; padding: 2px 12px;
    border: 2px solid var(--gold); font-size: 36px; font-weight: 600; letter-spacing: 2px; line-height: 1.3;
  }
  .schedule {
    position: absolute; left: 40px; top: 968px; padding-left: 22px;
    border-left: 3px solid var(--gold); font-family: "Cormorant Garamond", serif;
    font-weight: 600; color: var(--gold); line-height: 1; font-variant-numeric: lining-nums;
  }
  .schedule-time { font-size: 60px; letter-spacing: 2px; }
  .schedule-open { font-size: 60px; letter-spacing: 2px; margin-top: 16px; }
  .venue {
    position: absolute; left: 568px; top: 966px; padding-left: 0;
    color: var(--gold); line-height: 1.45;
  }
  .venue-name, .venue-access { font-size: 27px; font-weight: 600; letter-spacing: 1px; }
  .venue-lines { font-size: 18px; font-weight: 500; margin-top: 4px; }
</style>
</head>
<body>
<main class="poster">
  <div class="hero-visual" role="img" aria-label="宇宙から見た地球の地平線と、そこから昇る強い光のビジュアル"></div>

  <h1>
    <span class="title-en title-en--first">BILLIONAIRE</span>
    <span class="title-en title-en--second">LESSON</span>
  </h1>
  <svg class="divider-slash" width="851" height="260" aria-hidden="true">
    <line x1="566" y1="226" x2="648" y2="146" stroke="var(--gold)" stroke-width="2"/>
  </svg>
  <p class="title-ja">ビリオネアの授業 2018</p>

  <p class="catch catch--first">桁違いの</p>
  <p class="catch catch--second">億万長者になるには</p>

  <div class="date">
    <span class="date-year">2018</span>
    <span class="date-day">9.17</span>
    <span class="date-week"><span>月</span><span class="holiday">祝</span></span>
  </div>
  <p class="tour-label">来日公演</p>

  <div class="schedule">
    <p class="schedule-time">13:00 ····· 19:30</p>
    <p class="schedule-open">OPEN／12:00</p>
  </div>

  <div class="venue">
    <p class="venue-name">中之島記念ホール</p>
    <p class="venue-access">北浜通駅 徒歩５分</p>
    <p class="venue-lines">地下鉄みなと線／湾岸電鉄本線</p>
  </div>
</main>
</body>
</html>
```